Squarespace website build: Quill literary annual (initial design work supplied)

Our brand guidelines provide the look and feel for the website - we just need someone to create it based on our mock ups!
PLEASE NOTE:
- Please base our website off the website pages within the brief (ie homepage is GREEN)
- please ensure each page will be standalone (not a scrolling home page)
- please only use filtered duotone style photography as a hold, if you think the page needs a photo.
-please not the websites i have provided as an influence - especially BRINE ANNUAL. We want very little photography.

Quill is a literary and arts journal that provides a platform for both emerging and established writers and artists from New Zealand and beyond. We are passionate about sharing insights into the intimate and unique worlds of creatives with short stories, poetry, and art – showcasing raw and unfiltered glimpses into their world.

We have our brand guidelines and logo finalised, with a 'look and feel' design for the website within our attached brand guidelines document. We just need someone to design this simple website on Squarespace for us. It will have five pages and will need a newsletter sign up link:
Home page
About us page
Submissions page
Purchase page
Contact page

DRAFT WEB COPY

ABOUT
QUILL is an independent literary annual journal established in 2022 by Harriet Calloway and Mereana Platt that publishes unrepentant unfiltered accounts of life, eclectic takes on the mundane ordinary, and deep dives into modern love & sexuality.
Founder, Editor: Harriet Anahera Calloway
Founder, Production Director: Mereana Platt
Art Direction: Corin Ashby
Editorial Assistant: Lucy Fenwick-Dorsey

I suggest duotone fashion-esque photography which is very Marla Quiggin/ Palm Springs vibe but not obviously identifiable.
· I love the style of Rex Havelin for our shoot in particular. Group lazing around a pool, leisurely, glam, but effortless and ironically looking very natural – as though – yes, these are our lives.
SUBMISSION PAGE
Quill welcomes submissions all year round.
We are drawn to dark humour, satirical takes on the social scene, and starkly honest accounts of ordinary life. Diversity is celebrated, adversity is welcomed and, above all, personal expression is championed. We are particularly seeking content that takes risks, screams of honesty and celebrates life’s most extraordinary moments.
Selected works will be published in our annual publication.

Submission guidelines
We accept flash fiction, short stories and poetry. Individual entries not to mustn’t exceed 2000 words.
Submitted work must be unpublished and in English. We welcome simultaneous submissions, but must be notified immediately if your manuscript is accepted for publication elsewhere or appears in any print or online source. We will endeavour to respond to all submissions within four weeks.
Please send submissions as a word document along with a brief bio of 50 words to inkwell@quilljournal.example
PO Box[EB2]
​Note on Copyright: Copyright remains with the author.

Annual short story competition
Issue One is interested in all that is spiritual, coincidental, or mysterious. Stories selected for this issue reflect life’s uncanny moments, those that defy explanation, and experiences that promote personal and spiritual growth. Entires must be no longer than 2000 words.

First prize: 1000
Second prize: 500
Third prize: 200[EB3]

SUPPORT US
Since our launch in 2022, we have relied upon the generous support of our creative business community in Wellington City, New Zealand. If you read us, or love our ethos, please consider a donation.
Link to chipinhere page
Updates

Hello designers
I would ideally love to have someone turn this around within a few weeks, because the design work has mostly been provided.
Thanks
Harriet

Hi everyone Please ensure you read our brand guidelines and follow the brief. Please note we do not yet have a product, as this is a new venture, so there is no point including images of a magazine that doesn't yet exist. Some further comment to ensure we get there: - We want all pages to be separate pages (not a scrolling home page) with a different colour based on the guidelines - The home page must look just as it does in the brand guidelines - There is no archive page (please read brief) as we have no archive yet. The pages are: Home, About, Contact, Competitions and submissions Thank you

Target Market(s)

writers and creatives

Industry/Entity Type

Writing/ creative/ publishing

Coding

Coded - Design and coding required

Number of Pages Required

4 page

Font styles to use
Other font styles liked:
• COTTA and Univers - as per brand guidelines

Requirements
Must have
• Squarespace designer needed to design our mocked up webpages.
Nice to have
• As close to the brand guideline mock ups as possible (see page 11,12,13)
Should not have
• anything outside of the brand guidelines

```html
<!DOCTYPE html>
<html lang="en">
<head>
<meta charset="utf-8">
<title>Quill — Literary Annual</title>
<link rel="stylesheet" href="https://fonts.googleapis.com/css2?family=Marcellus&family=Oswald:wght@300;400&family=Heebo:wght@300;400&display=swap">
<style>
:root{
  --cream:#f4ebdf;
  --plum:#6c4262;
  --plum-dark:#5c3554;
  --rose:#c2506f;
  --rose-band:#c06f84;
  --mustard:#c4a516;
  --olive:#4f6b2a;
  --photo-gold:#b09a3e;
  --ink:#4a4a4a;
  --dark:#222222;
  --darker:#1a1a1a;
  --white:#ffffff;
}
*{margin:0;padding:0;box-sizing:border-box}
html,body{width:1200px;height:2997px;overflow:hidden}
body{background:var(--cream);font-family:"Heebo",Arial,sans-serif;color:var(--ink);position:relative}
.abs{position:absolute}
.serif{font-family:"Marcellus",Georgia,serif}
.btn{position:absolute;display:flex;align-items:center;gap:12px;padding:0 22px;height:41px;background:var(--rose);color:var(--white);font-size:14px;text-decoration:none}
.btn svg{width:22px;height:10px}
.wordmark{font-family:"Marcellus",Georgia,serif;color:var(--rose);font-size:54px;line-height:1;letter-spacing:1px}
.nav{display:flex;gap:38px;font-size:14px;color:#333}
.nav a{color:inherit;text-decoration:none}
.nav .active{border-bottom:1px solid #333;padding-bottom:4px}
.dots{letter-spacing:5px;color:var(--rose);font-size:14px;line-height:1}
.section-title{font-family:"Marcellus",Georgia,serif;color:var(--plum);font-size:32px;line-height:1.2}
.icon-circle{width:40px;height:40px;border-radius:50%;background:var(--rose);display:flex;align-items:center;justify-content:center}
.icon-circle svg{width:20px;height:20px}
.cover{position:absolute;border:1px solid var(--mustard)}
.cover-fill{position:absolute;background:linear-gradient(180deg,var(--mustard) 0 32%,var(--olive) 32% 100%)}
.prize{position:absolute;background:var(--cream);text-align:center;padding-top:44px}
.prize .amount{font-family:"Oswald",sans-serif;font-weight:400;font-size:50px;color:#222;line-height:1}
.prize .rule{width:36px;height:1px;background:var(--rose);margin:18px auto 12px}
.prize .place{font-size:21px;color:#222;letter-spacing:.5px}
.prize p{font-size:13px;line-height:1.55;margin-top:12px;padding:0 22px;color:#444}
.credit .role{font-size:13px;letter-spacing:.5px;color:#333}
.credit .name{font-family:"Oswald",sans-serif;font-weight:300;font-size:18px;color:#222;margin-top:3px}
.contact-label{font-family:"Oswald",sans-serif;font-weight:300;color:var(--white);font-size:17px;letter-spacing:2px}
.contact-text{color:var(--white);font-size:14px;line-height:1.6;margin-top:6px}
</style>
</head>
<body>

<!-- Header -->
<header>
  <div class="abs wordmark" style="left:162px;top:16px">quill</div>
  <nav class="abs nav" style="left:398px;top:37px">
    <a class="active">Home</a><a>About Us</a><a>Submissions</a><a>Purchase</a><a>Contact Us</a>
  </nav>
  <div class="abs icon-circle" style="left:871px;top:24px">
    <svg viewBox="0 0 24 24" fill="none" stroke="#fff" stroke-width="1.6"><path d="M5 3h4l2 5-3 2a12 12 0 0 0 6 6l2-3 5 2v4a2 2 0 0 1-2 2A17 17 0 0 1 3 5a2 2 0 0 1 2-2z"/></svg>
  </div>
  <div class="abs" style="left:917px;top:25px;font-size:12px;letter-spacing:3px;color:#333">CALL US TODAY</div>
  <div class="abs serif" style="left:917px;top:42px;font-size:20px;color:var(--rose);letter-spacing:1px">123&nbsp; 456 7890</div>
</header>

<!-- Hero -->
<section class="hero">
  <h1 class="abs serif" style="left:162px;top:236px;width:460px;font-weight:400;font-size:31px;line-height:45px;color:var(--plum)">QUILL IS A PLUCKY LITTLE PUBLICATION OUT OF WELLINGTON, NEW ZEALAND</h1>
  <a class="btn" style="left:162px;top:388px">Contact Us <svg viewBox="0 0 22 10" fill="none" stroke="#fff"><path d="M0 5h21M16 1l5 4-5 4"/></svg></a>
  <div class="cover" style="left:625px;top:151px;width:413px;height:430px;border-bottom:none"></div>
  <div class="cover-fill" role="img" aria-label="Duotone issue cover with portrait of a woman in glasses" style="left:637px;top:165px;width:386px;height:416px"></div>
</section>

<!-- Newsletter -->
<section class="abs" role="img" aria-label="Plum newsletter band with soft block texture" style="left:0;top:581px;width:1200px;height:264px;background:linear-gradient(90deg,var(--plum-dark),var(--plum) 30%,#7a4e70 55%,var(--plum) 80%,var(--plum-dark))">
  <h2 class="abs serif" style="left:0;top:64px;width:1200px;text-align:center;font-weight:400;font-size:31px;color:var(--white)">SUBSCRIBE TO OUR NEWSLETTER</h2>
  <p class="abs" style="left:0;top:106px;width:1200px;text-align:center;font-size:14px;color:var(--white)">Sign Up to Know More About Our News</p>
  <div class="abs" style="left:428px;top:150px;width:226px;height:36px;background:var(--white);font-size:12px;color:#999;padding:11px 12px">Email Address</div>
  <a class="btn" style="left:661px;top:150px;height:36px;width:128px;padding:0 18px;background:var(--mustard)">Subscribe <svg viewBox="0 0 22 10" fill="none" stroke="#fff"><path d="M0 5h21M16 1l5 4-5 4"/></svg></a>
</section>

<!-- About -->
<section class="about">
  <svg class="abs" style="left:133px;top:905px" width="106" height="106" viewBox="0 0 106 106" fill="none" stroke="var(--rose)" stroke-width="1.4"><path d="M105 2H12M12 2v100"/></svg>
  <svg class="abs" style="left:468px;top:1307px" width="106" height="106" viewBox="0 0 106 106" fill="none" stroke="var(--rose)" stroke-width="1.4"><path d="M94 2v100H0"/></svg>
  <div class="abs" role="img" aria-label="Duotone photo of a woman with curly hair writing in a notebook" style="left:162px;top:934px;width:390px;height:456px;background:linear-gradient(135deg,#b8a44a,var(--photo-gold) 55%,#9c8a3a)"></div>
  <h2 class="abs section-title" style="left:608px;top:928px;font-weight:400">ABOUT QUILL</h2>
  <div class="abs dots" style="left:608px;top:970px">......</div>
  <p class="abs" style="left:609px;top:1003px;width:432px;font-size:13px;line-height:21.5px;color:#555">QUILL is an independent literary annual journal established in 2022 by Harriet Calloway and Mereana Platt that publishes unrepentant unfiltered accounts of life, eclectic takes on the mundane ordinary, and deep dives into modern love &amp; sexuality.</p>
  <div class="abs credit" style="left:611px;top:1102px"><div class="role">Founder, Editor:</div><div class="name">Harriet Anahera Calloway</div></div>
  <div class="abs credit" style="left:611px;top:1160px"><div class="role">Founder, Production Director:</div><div class="name">Mereana Platt</div></div>
  <div class="abs credit" style="left:611px;top:1218px"><div class="role">Art Direction:</div><div class="name">Corin Ashby</div></div>
  <div class="abs credit" style="left:611px;top:1276px"><div class="role">Editorial Assistant:</div><div class="name">Lucy Fenwick-Dorsey</div></div>
  <a class="btn" style="left:612px;top:1336px;width:143px">Read More <svg viewBox="0 0 22 10" fill="none" stroke="#fff"><path d="M0 5h21M16 1l5 4-5 4"/></svg></a>
</section>

<!-- Competition -->
<section class="abs" role="img" aria-label="Rose band with open magazines laid in the background" style="left:0;top:1541px;width:1200px;height:608px;background:linear-gradient(100deg,var(--rose-band),#c56f82 50%,#cb7170 80%,var(--rose-band))">
  <h2 class="abs serif" style="left:0;top:70px;width:1200px;text-align:center;font-weight:400;font-size:31px;color:var(--white)">ANNUAL SHORT STORY COMPETITION</h2>
  <div class="abs dots" style="left:0;top:108px;width:1200px;text-align:center;color:var(--white)">......</div>
  <p class="abs" style="left:266px;top:142px;width:668px;text-align:center;font-size:13.5px;line-height:22px;color:var(--white)">Issue One is interested in all that is spiritual, coincidental, or mysterious. Stories selected for this issue reflect life’s uncanny moments, those that defy explanation, and experiences that promote personal and spiritual growth. Entires must be no longer than 2000 words.</p>
  <div class="prize" style="left:234px;top:256px;width:225px;height:248px">
    <div class="amount">$500</div><div class="rule"></div><div class="place">Second prize</div>
    <p>Lorem ipsum dolor sit amet, consectetur adipiscing elit. Nullam et odio dignissim</p>
  </div>
  <div class="prize" style="left:496px;top:233px;width:226px;height:290px">
    <div class="amount">$1000</div><div class="rule"></div><div class="place">First Prize</div>
    <p>Lorem ipsum dolor sit amet, consectetur adipiscing elit. Nullam et odio dignissim est tristique rutrum.</p>
  </div>
  <div class="prize" style="left:761px;top:261px;width:226px;height:248px">
    <div class="amount">$200</div><div class="rule"></div><div class="place">Third Prize</div>
    <p>Lorem ipsum dolor sit amet, consectetur adipiscing elit. Nullam et odio dignissim</p>
  </div>
</section>

<!-- Support -->
<section class="support">
  <h2 class="abs section-title" style="left:161px;top:2338px;font-weight:400">SUPPORT US</h2>
  <div class="abs dots" style="left:161px;top:2380px">......</div>
  <p class="abs" style="left:162px;top:2412px;width:420px;font-size:16px;line-height:26.5px;font-weight:300;color:#444">Since our launch in 2022, we have relied upon the generous support of our creative business community in Wellington City, New Zealand. If you read us, or love our ethos, please consider a donation.</p>
  <a class="btn" style="left:162px;top:2537px;width:151px">Donate Now <svg viewBox="0 0 22 10" fill="none" stroke="#fff"><path d="M0 5h21M16 1l5 4-5 4"/></svg></a>
  <div class="cover" style="left:672px;top:2279px;width:368px;height:382px;border-bottom:none"></div>
  <div class="cover-fill" role="img" aria-label="Duotone issue cover with portrait of a woman in glasses" style="left:683px;top:2291px;width:345px;height:370px"></div>
</section>

<!-- Footer -->
<footer class="abs" style="left:0;top:2661px;width:1200px;height:336px;background:var(--dark)">
  <div class="abs wordmark" style="left:162px;top:60px">quill</div>
  <nav class="abs nav" style="left:593px;top:84px;color:var(--white);gap:37px"><a>Home</a><a>About Us</a><a>Submissions</a><a>Purchase</a><a>Contact Us</a></nav>

  <div class="abs icon-circle" style="left:162px;top:168px"><svg viewBox="0 0 24 24" fill="none" stroke="#fff" stroke-width="1.6"><path d="M12 21s-6-6.5-6-11a6 6 0 0 1 12 0c0 4.5-6 11-6 11z"/><circle cx="12" cy="10" r="2.2"/></svg></div>
  <div class="abs" style="left:214px;top:168px"><div class="contact-label">ADDRESS</div><div class="contact-text">123 Building Name, Street,<br>City Name, State XY-123456</div></div>

  <div class="abs icon-circle" style="left:541px;top:168px"><svg viewBox="0 0 24 24" fill="none" stroke="#fff" stroke-width="1.6"><path d="M5 3h4l2 5-3 2a12 12 0 0 0 6 6l2-3 5 2v4a2 2 0 0 1-2 2A17 17 0 0 1 3 5a2 2 0 0 1 2-2z"/></svg></div>
  <div class="abs" style="left:594px;top:168px"><div class="contact-label">PHONE</div><div class="contact-text" style="font-size:17px">123&nbsp; 456 7890</div></div>

  <div class="abs icon-circle" style="left:867px;top:168px"><svg viewBox="0 0 24 24" fill="none" stroke="#fff" stroke-width="1.6"><rect x="3" y="5" width="18" height="14" rx="1"/><path d="M3 6l9 7 9-7"/></svg></div>
  <div class="abs" style="left:920px;top:168px"><div class="contact-label">EMAIL</div><div class="contact-text" style="font-size:16px">hello@quilljournal.example</div></div>

  <div class="abs" style="left:0;top:293px;width:1200px;height:43px;background:var(--darker)">
    <p class="abs" style="left:162px;top:13px;font-size:13px;color:#ccc">Copyright 2022 Quill. All Rights Reserved.</p>
    <div class="abs" style="left:923px;top:10px;display:flex;gap:8px">
      <span style="width:22px;height:22px;border-radius:50%;background:#333"></span>
      <span style="width:22px;height:22px;border-radius:50%;background:#333"></span>
      <span style="width:22px;height:22px;border-radius:50%;background:#333"></span>
      <span style="width:22px;height:22px;border-radius:50%;background:#333"></span>
    </div>
  </div>
</footer>

</body>
</html>
```